RDW Drifting Marigold, American Quarter Horse Stallion Stud Services

Advertisement for stud service. I'd like to showcase how stunningly beautiful this horse is with the full-body pic and how sweet, gentle, and quiet he is with the other pic. I want two-sided cards with photos on both sides. Headshot (cropped) on front with info on management, contact #s, etc. Full-body, pairup.example-type pic on back with some information on his pedigree. I'd like something striking enough that even if people don't want the service, they keep the card.

Target Market(s)

Horse owners, horse breeders, horse trainers, equestrians

Contact Information for Business Card

Horse's name: RDW Drifting Marigold
Owner: Noreen Castell
Manager: Trudy Wexmoor
Phone: 208-555-0148
Pedigree information: Sire - Oaks Bonne Lucette, Dam - Quiet Dancing Lorabel
Sire's parents: Brightwater Tam 41 (sire) and Cedar Gentle Lass (dam)
Dam's parents: Shez Dorabel (sire) and Bold Hearted Rhyme (dam)

Font styles to use
Sans Serif

Requirements
Must have
• Rich, distinctive look. Should be a stand-out card; one that people keep even if they're not interested in the service.
Nice to have
• Pedigree information displayed in a family-tree arrangement. The horse is black, so I am picturing cards that are mostly black, probably with white or off-white (cream-colored) lettering. In fact, the horse has what's known as the cream-color gene, so maybe cream-colored would be better.

```html
<!DOCTYPE html>
<html lang="en">
<head>
<meta charset="utf-8">
<title>RDW Drifting Marigold – Pedigree Card</title>
<link rel="stylesheet" href="https://fonts.googleapis.com/css2?family=Source+Sans+3:ital,wght@0,400;0,600;1,700&display=swap">
<style>
  :root {
    --backdrop: #d1d2d4;
    --card-cream: #fffbef;
    --ink: #231f1c;
    --bracket-brown: #8a7358;
    --bar-black: #111111;
    --sky: #c9d2d6;
    --treeline: #6d6a4e;
    --pasture: #5e8a3c;
    --arena: #b3a48a;
    --photo-dark: #121212;
  }
  * { box-sizing: border-box; margin: 0; padding: 0; }
  html, body {
    width: 1194px; height: 1200px; overflow: hidden;
    background: var(--backdrop);
  }
  .pedigree-card {
    position: absolute; left: 72px; top: 290px;
    width: 1050px; height: 620px;
    background: var(--card-cream);
    font-family: "Source Sans 3", sans-serif;
    color: var(--ink);
    box-shadow: 0 2px 6px rgba(0,0,0,0.12);
    overflow: hidden;
  }
  .tree-lines { position: absolute; left: 0; top: 0; width: 420px; height: 620px; }
  .ancestor {
    position: absolute; font-size: 24px; font-weight: 400;
    line-height: 1; white-space: nowrap; transform: translateY(-50%);
  }
  .ancestor--grandparent { left: 30px; }
  .ancestor--parent { left: 46px; }
  .stallion-name {
    position: absolute; left: 76px; top: 313px; transform: translateY(-50%);
    font-size: 32px; font-weight: 700; font-style: italic;
    line-height: 1; white-space: nowrap;
  }
  .stallion-photo {
    position: absolute; left: 425px; top: 30px;
    width: 615px; height: 562px;
    background: linear-gradient(180deg,
      var(--sky) 0%, var(--treeline) 22%, var(--pasture) 42%,
      var(--photo-dark) 52%, var(--pasture) 66%, var(--arena) 78%, var(--arena) 100%);
    box-shadow: inset 0 0 40px 22px var(--card-cream);
  }
</style>
</head>
<body>
  <article class="pedigree-card">
    <svg class="tree-lines" viewBox="0 0 420 620" aria-hidden="true">
      <rect x="2" y="30" width="8" height="100" fill="var(--bar-black)"/>
      <rect x="2" y="486" width="8" height="100" fill="var(--bar-black)"/>
      <g fill="none" stroke="var(--bracket-brown)" stroke-width="3">
        <polyline points="268,51 290,51 290,116 268,116"/>
        <line x1="290" y1="83" x2="312" y2="83"/>
        <polyline points="64,236 56,236 56,390 64,390"/>
        <line x1="56" y1="313" x2="68" y2="313"/>
        <polyline points="268,420 290,420 290,566 268,566"/>
        <line x1="290" y1="493" x2="312" y2="493"/>
      </g>
    </svg>

    <span class="ancestor ancestor--grandparent" style="top:51px">Brightwater Tam 41</span>
    <span class="ancestor ancestor--grandparent" style="top:116px">Cedar Gentle Lass</span>
    <span class="ancestor ancestor--parent" style="top:215px">Oaks Bonne Lucette</span>
    <h1 class="stallion-name">RDW Drifting Marigold</h1>
    <span class="ancestor ancestor--parent" style="top:412px">Quiet Dancing Lorabel</span>
    <span class="ancestor ancestor--grandparent" style="top:506px">Shez Dorabel</span>
    <span class="ancestor ancestor--grandparent" style="top:570px">Bold Hearted Rhyme</span>

    <div class="stallion-photo" role="img" aria-label="Full-body photo of the black Quarter Horse stallion standing in profile in a sunny arena, trees and pasture behind"></div>
  </article>
</body>
</html>
```